Tor Brook Healthcare of Lauderhill

A website design for this primary care physician practice, featuring latino, caucasian and black patients and employees.

Target Market(s)

LATIN, INDIAN, ASIAN, CARIBBEAN/BLACK, AND CAUCASIAN PATIENTS.

Coding

Coded - Design and coding required

Number of Pages Required

4 page

Requirements
Must have
• 1. MULTICULTURAL PICTURES OF PATIENTS AND EMPLOYEES
• 2. About Us
• We specialize in internal medicine and offer a full range of primary care and family medical services. We are dedicated to your well-being and ensure continuity of care every time you visit our office. Our staff works with patients to understand their lifestyle and needs to continually deliver the best care possible. If you are looking for a primary healthcare provider and a quality experience, feel free to contact us to schedule an appointment today.
• Family Health Care
• Our clinical team is ready to serve the entire family and provide the most advanced and personalized care available today.
• 3. Schedule An Appointment
• We are open Monday through Friday from 9am to 4:30pm.
• Same Day Availability
• 4. Our focus is to provide our patients with life-long care and to be readily available for immediate and unexpected emergencies.
• Flu, Headaches and Pain
• Everyday illnesses, aches and pains can set you back at work and at home. Our commitment is to get you back to your daily activities quickly.
• 5. Chronic Disease Management
• Many people suffer from numerous types of chronic diseases every day, and when it comes to chronic disease management, early detection and treatment are crucial to living a healthy life. Helping Patients Live the Most Active Life Possible. So here at Tor-Brook Health Care, we take pride in serving patients who suffer from chronic diseases and help them live the most active life possible.
• If you are already diagnosed or think you may have a potential issue, come see us to receive help and start managing your chronic disease. We take pride in delivering personalized care for life. We see you through more than just doctor’s appointment, we take care of you through it all.
• Chronic Diseases We Treat
• Fibromyalgia Congestive Heart Failure
• High Blood Pressure Congestive Obstructive Pulmonary Disease
• High Cholesterol
• Diabetes
• 6. Our Founder, Dr. Marcus Verlaine
• Why I Became an Internal Medicine Doctor
• I chose Primary Care Internal Medicine because I wanted to get to know patients over time, to see a broad array of different kinds of illnesses, treat the whole patient (not just one body part), learn and help with the physical and mental health of my patients and most importantly, form relationships with them.
• I would love to meet you and would be honored if you choose me as your primary care physician. I chose Internal Medicine for my residency because in Internal Medicine the focus is on adults and more complex patients.
• I have enjoyed the more than 25 years I have spent as an internal medicine doctor and I am very happy with the patient relationships I have established in the course of my practice. I would love to meet you and would be honored if you choose me as your primary care physician.
• Marcus Verlaine, MD
• 7. Locations
• Tor-Brook Healthcare Center
• 3172 Palm Crest Rd
• Greenacres, Florida 33463
• Office: (561) 555-0182
• Fax: (561) 555-0147
• 5300 W. Harbor Blvd, Suite 104
• Lauderhill, Florida 33319
• Office: (954) 555-0163
• Fax: (954) 555-0129
• * Both locations are open Monday through Friday from 9am to 4:30pm.
Nice to have
• BRIGHT FLORIDA/CARIBBEAN COLORS

```html
<!DOCTYPE html>
<html lang="en">
<head>
<meta charset="utf-8">
<title>Tor Brook Healthcare</title>
<link rel="stylesheet" href="https://fonts.googleapis.com/css2?family=Lato:wght@400;700;900&family=Open+Sans:wght@400;600;700&display=swap">
<style>
:root{
  --blue:#1e96d4;
  --blue-dark:#1474b0;
  --green:#8cc63f;
  --green-dark:#76ad2c;
  --ink:#1d1d1d;
  --text:#555;
  --muted:#888;
  --light:#f3f4f6;
  --line:#dcdcdc;
  --white:#fff;
}
*{box-sizing:border-box;margin:0;padding:0}
html,body{width:1200px;height:3814px;overflow:hidden}
body{font-family:"Open Sans",sans-serif;color:var(--text);background:var(--white);position:relative}
.sec{position:absolute;left:0;width:1200px}
h1,h2,h3,h4{font-family:"Lato",sans-serif}

/* top bar */
.topbar{top:0;height:25px;background:var(--blue);color:#fff;font-size:11px;display:flex;align-items:center;justify-content:space-between;padding:0 100px}
.topbar .group{display:flex;gap:14px;align-items:center}
.dot{display:inline-block;width:9px;height:9px;border-radius:50%;background:#fff;margin-right:4px;vertical-align:middle}

/* header */
.header{top:25px;height:102px;display:flex;align-items:center;justify-content:space-between;padding:0 100px}
.brand{display:flex;align-items:center;gap:12px;font-family:"Lato",sans-serif;font-weight:700;font-size:20px;color:var(--ink)}
.brand .mark{width:40px;height:40px;border-radius:50%;background:var(--green)}
.nav{display:flex;align-items:center;gap:26px;font-size:14px;font-weight:600;color:var(--ink)}
.nav .active{color:var(--green)}
.login{background:var(--green);color:#fff;border-radius:16px;padding:6px 18px;font-size:12px}

/* hero */
.hero{top:127px;height:519px;background:linear-gradient(180deg,#d99a4f 0%,#8a7a74 35%,#3f5b6d 65%,#2f4a3a 100%);text-align:center;color:#fff}
.hero h1{margin-top:165px;font-size:48px;font-weight:900;letter-spacing:1px}
.hero p{font-family:"Lato",sans-serif;font-size:24px;font-weight:700;line-height:38px;margin:16px auto 0;width:640px}
.btn{display:inline-block;background:var(--green);color:#fff;font-family:"Lato",sans-serif;font-weight:700;border-radius:30px}
.hero .btn{margin-top:26px;padding:14px 34px;font-size:16px}
.arrow{position:absolute;top:238px;width:48px;height:48px;border-radius:50%;background:rgba(255,255,255,.3);display:flex;align-items:center;justify-content:center}

/* excellence */
.excellence{top:646px;height:498px}
.excellence h2{position:absolute;left:96px;top:90px;font-size:31px;font-weight:700;color:var(--ink)}
.excellence .lead{position:absolute;left:96px;top:148px;width:500px;color:var(--blue);font-size:18px;font-weight:600;line-height:30px}
.excellence .body{position:absolute;left:96px;top:228px;width:510px;font-size:13px;line-height:22px}
.excellence .btn{position:absolute;left:96px;top:372px;padding:10px 22px;font-size:13px}
.photo-frame{position:absolute;left:648px;top:96px;width:450px;height:338px;border:6px solid #fff;box-shadow:0 2px 12px rgba(0,0,0,.18);background:linear-gradient(135deg,#9ec9e6,#4d7fa6 60%,#2c4f6d)}

/* schedule */
.schedule{top:1144px;height:269px;background:linear-gradient(90deg,#8c7a70,#b9a89a 50%,#7d6f68);text-align:center;color:#fff}
.schedule h2{margin-top:80px;font-size:33px;font-weight:900}
.schedule p{font-size:16px;margin-top:8px}
.schedule .sub{font-size:18px;margin-top:26px;font-weight:600}

/* focus */
.focus{top:1413px;height:570px;text-align:center}
.focus h2{margin:96px auto 0;width:900px;font-size:19px;font-weight:700;color:var(--ink);line-height:34px}
.focus p{margin-top:20px;font-size:14px}
.care-card{position:absolute;top:247px;width:305px;height:226px;background:#fff;border:1px solid var(--line);padding:6px}
.care-card .img{height:166px}
.care-card .label{height:42px;background:var(--blue);color:#fff;font-family:"Lato",sans-serif;font-size:19px;display:flex;align-items:center;justify-content:center}

/* chronic */
.chronic{top:1983px;height:602px;background:var(--light);text-align:center}
.chronic h2{margin-top:88px;font-size:31px;font-weight:700;color:var(--ink)}
.chronic .copy{width:1000px;margin:28px auto 0;font-size:12.5px;line-height:22px;color:var(--muted)}
.chronic .copy+.copy{margin-top:16px}
.disease{position:absolute;top:389px;width:305px;height:201px;background:#fff;border:1px solid var(--line);display:flex;flex-direction:column;align-items:center;padding-top:36px}
.disease h4{font-size:16px;font-weight:700;color:var(--ink);line-height:28px;margin-top:16px}
.chev{position:absolute;top:465px;color:#777;font-size:28px}

/* founder */
.founder{top:2585px;height:415px;background:linear-gradient(90deg,#1e8fd4 0%,#2aa3c9 45%,#7fc24a 80%,#8cc63f 100%);color:#fff}
.portrait{position:absolute;left:106px;top:82px;width:170px;height:170px;border-radius:50%;border:6px solid #fff;background:linear-gradient(160deg,#dce8f2,#98b5cc)}
.founder .name{position:absolute;left:56px;top:280px;width:270px;text-align:center;font-family:"Lato",sans-serif;font-size:19px}
.founder h2{position:absolute;left:378px;top:72px;font-size:31px;font-weight:900}
.founder h3{position:absolute;left:378px;top:122px;font-size:20px;font-weight:700}
.founder .bio{position:absolute;left:378px;top:170px;width:720px;font-size:12.5px;line-height:22px}

/* contact */
.contact{top:3000px;height:498px;text-align:center}
.contact h2{margin-top:92px;font-size:31px;font-weight:700;color:var(--ink)}
.contact .intro{font-size:12px;margin-top:14px}
.form{position:absolute;left:200px;top:190px;width:800px}
.row{display:flex;gap:20px}
.field{flex:1;height:46px;border:1px solid var(--line);text-align:left;padding:14px;font-size:12px;color:#999}
.field.msg{height:76px;margin-top:18px}
.contact .btn{position:absolute;left:519px;top:352px;padding:12px 36px;font-size:16px}

/* footer */
.footer{top:3498px;height:249px;background:linear-gradient(180deg,#1e8fd4,#3aa4dd);color:#fff}
.loc{position:absolute;top:38px}
.loc h4{font-size:16px;font-weight:700;margin-bottom:18px}
.loc .line{display:flex;gap:12px;font-size:11.5px;line-height:19px;margin-bottom:8px}
.loc svg{flex:none;margin-top:3px}
.bottom{top:3747px;height:67px;background:var(--green);color:#fff;font-size:13px;display:flex;align-items:center;justify-content:space-between;padding:0 100px}
.social{display:flex;gap:10px}
.social span{width:32px;height:32px;border-radius:50%;border:2px solid #fff}
</style>
</head>
<body>

<div class="sec topbar">
  <div class="group"><span><span class="dot"></span><span class="dot"></span><span class="dot"></span></span><span>Monday - Friday &nbsp;|&nbsp; 9am to 4:30pm.</span></div>
  <div class="group"><span>Quick Email</span><span>(+351) 900 555 012</span></div>
</div>

<header class="sec header">
  <div class="brand"><span class="mark"></span>Tor Brook Healthcare</div>
  <nav class="nav">
    <span class="active">Home</span><span>About Us</span><span>Our Services</span><span>Blog</span><span>Contact Us</span>
    <svg width="14" height="14" viewBox="0 0 14 14"><circle cx="6" cy="6" r="4.5" fill="none" stroke="#1d1d1d" stroke-width="2"/><path d="M9.5 9.5L13 13" stroke="#1d1d1d" stroke-width="2"/></svg>
    <span class="login">Login</span>
  </nav>
</header>

<section class="sec hero" role="img" aria-label="Sunset skyline of a Florida city with palm trees">
  <h1>TOR BROOK HEALTHCARE</h1>
  <p>Duis aute irure dolor in reprehenderit in voluptate velit essint occaecat cillum dolore eu fugiat sint occaecat nulla pariatur.</p>
  <span class="btn">CONTACT US</span>
  <span class="arrow" style="left:22px"><svg width="14" height="14"><path d="M10 1L3 7l7 6" fill="none" stroke="#fff" stroke-width="2.5"/></svg></span>
  <span class="arrow" style="right:22px"><svg width="14" height="14"><path d="M4 1l7 6-7 6" fill="none" stroke="#fff" stroke-width="2.5"/></svg></span>
</section>

<section class="sec excellence">
  <h2>EXCELLENCE IN HEALTHCARE</h2>
  <p class="lead">We specialize in internal medicine and offer a full range of primary care and family medical services.</p>
  <p class="body">We are dedicated to your well-being and ensure continuity of care every time you visit our office. Our staff works with patients to understand their lifestyle and needs to continually deliver the best care possible. If you are looking for a primary healthcare provider and a quality experience, feel free to contact us to schedule an appointment today.</p>
  <span class="btn">READ MORE ›</span>
  <div class="photo-frame" role="img" aria-label="Video still of doctor and nurse attending a patient"></div>
</section>

<section class="sec schedule" role="img" aria-label="Group of smiling multicultural medical staff">
  <h2>SCHEDULE AN APPOINTMENT</h2>
  <p>We are open Monday through Friday from 9am to 4:30pm.</p>
  <p class="sub">Same Day Availability</p>
</section>

<section class="sec focus">
  <h2>OUR FOCUS IS TO PROVIDE OUR PATIENTS WITH LIFE-LONG CARE AND TO BE READILY AVAILABLE FOR IMMEDIATE AND UNEXPECTED EMERGENCIES.</h2>
  <p>Our commitment is to get you back to your daily activities quickly.</p>
  <div class="care-card" style="left:102px"><div class="img" role="img" aria-label="Woman with the flu using a tissue" style="background:linear-gradient(135deg,#e9e1dc,#b99a8a)"></div><div class="label">Flu</div></div>
  <div class="care-card" style="left:447px"><div class="img" role="img" aria-label="Man holding his head with a headache" style="background:linear-gradient(135deg,#a7c08f,#5b4a40)"></div><div class="label">Headaches and Pain</div></div>
  <div class="care-card" style="left:793px"><div class="img" role="img" aria-label="Woman resting on a couch feeling unwell" style="background:linear-gradient(135deg,#d9c6c9,#b46c7a)"></div><div class="label">Everyday illnesses</div></div>
</section>

<section class="sec chronic">
  <h2>CHRONIC DISEASE MANAGEMENT</h2>
  <p class="copy">Many people suffer from numerous types of chronic diseases every day, and when it comes to chronic disease management, early detection and treatment are crucial to living a healthy life. Helping Patients Live the Most Active Life Possible. So here at Tor-Brook Health Care, we take pride in serving patients who suffer from chronic diseases and help them live the most active life possible.</p>
  <p class="copy">If you are already diagnosed or think you may have a potential issue, come see us to receive help and start managing your chronic disease. We take pride in delivering personalized care for life. We see you through more than just doctor’s appointment, we take care of you through it all.</p>
  <span class="chev" style="left:44px">‹</span><span class="chev" style="right:44px">›</span>
  <div class="disease" style="left:102px">
    <svg width="60" height="54" viewBox="0 0 60 54"><path d="M30 50L6 26C-2 16 6 2 18 4c6 1 10 6 12 10 2-4 6-9 12-10 12-2 20 12 12 22z" fill="var(--blue)"/><path d="M12 27h12l4-8 5 14 4-6h11" fill="none" stroke="#fff" stroke-width="3"/></svg>
    <h4>Fibromyalgia Congestive<br>Heart Failure</h4>
  </div>
  <div class="disease" style="left:447px">
    <svg width="64" height="54" viewBox="0 0 64 54"><rect x="4" y="6" width="42" height="36" rx="8" fill="var(--blue)"/><circle cx="25" cy="24" r="11" fill="#fff"/><circle cx="25" cy="24" r="5" fill="var(--green)"/><path d="M46 24c10 0 14 10 10 20" fill="none" stroke="var(--blue)" stroke-width="3"/></svg>
    <h4>High Blood Pressure Congestive<br>Obstructive Pulmonary Disease</h4>
  </div>
  <div class="disease" style="left:793px">
    <svg width="56" height="56" viewBox="0 0 56 56"><g transform="rotate(-45 28 28)"><rect x="6" y="18" width="44" height="20" rx="10" fill="var(--blue)"/><rect x="28" y="18" width="22" height="20" rx="10" fill="var(--green)"/><rect x="28" y="18" width="8" height="20" fill="var(--green)"/></g></svg>
    <h4>High Cholesterol</h4>
  </div>
</section>

<section class="sec founder">
  <div class="portrait" role="img" aria-label="Portrait of the founding physician in a white coat"></div>
  <div class="name">Marcus Verlaine, MD</div>
  <h2>OUR FOUNDER</h2>
  <h3>Dr. Marcus Verlaine, Why I Became an Internal Medicine Doctor.</h3>
  <p class="bio">I chose Primary Care Internal Medicine because I wanted to get to know patients over time, to see a broad array of different kinds of illnesses, treat the whole patient (not just one body part), learn and help with the physical and mental health of my patients and most importantly, form relationships with them. I would love to meet you and would be honored if you choose me as your primary care physician. I chose Internal Medicine for my residency because in Internal Medicine the focus is on adults and more complex patients. I have enjoyed the more than 25 years I have spent as an internal medicine doctor and I am very happy with the patient relationships I have established in the course of my practice. I would love to meet you and would be honored if you choose me as your primary care physician.</p>
</section>

<section class="sec contact">
  <h2>QUICK CONTACT</h2>
  <p class="intro">It's on you how you want to live your life. Everyone has a choice. I pick my choice.</p>
  <div class="form">
    <div class="row"><div class="field">Enter Name</div><div class="field">Email Address</div><div class="field">Phone</div></div>
    <div class="field msg">Message</div>
  </div>
  <span class="btn">SUBMIT NOW</span>
</section>

<footer class="sec footer">
  <div class="loc" style="left:158px">
    <h4>Tor-Brook Healthcare Center</h4>
    <div class="line"><svg width="12" height="16" viewBox="0 0 12 16"><path d="M6 0a6 6 0 0 0-6 6c0 4 6 10 6 10s6-6 6-10a6 6 0 0 0-6-6z" fill="#fff"/><circle cx="6" cy="6" r="2" fill="var(--blue)"/></svg><span>3172 Palm Crest Rd<br>Greenacres, Florida 33463</span></div>
    <div class="line"><svg width="12" height="14" viewBox="0 0 12 14"><path d="M2 0h3l1 4-2 1c1 2 2 3 4 4l1-2 3 1v3c0 1-1 2-2 2C4 13-1 8 0 2c0-1 1-2 2-2z" fill="#fff"/></svg><span>Office: (561) 555-0182</span></div>
    <div class="line"><svg width="12" height="12" viewBox="0 0 12 12"><rect x="1" y="3" width="10" height="8" fill="#fff"/><rect x="3" y="0" width="6" height="4" fill="#fff"/></svg><span>Fax: (561) 555-0147</span></div>
  </div>
  <div class="loc" style="left:488px">
    <h4>Tor-Brook Healthcare Center</h4>
    <div class="line"><svg width="12" height="16" viewBox="0 0 12 16"><path d="M6 0a6 6 0 0 0-6 6c0 4 6 10 6 10s6-6 6-10a6 6 0 0 0-6-6z" fill="#fff"/><circle cx="6" cy="6" r="2" fill="var(--blue)"/></svg><span>5300 W. Harbor Blvd, Suite 104<br>Lauderhill, Florida 33319</span></div>
    <div class="line"><svg width="12" height="14" viewBox="0 0 12 14"><path d="M2 0h3l1 4-2 1c1 2 2 3 4 4l1-2 3 1v3c0 1-1 2-2 2C4 13-1 8 0 2c0-1 1-2 2-2z" fill="#fff"/></svg><span>Office: (954) 555-0163</span></div>
    <div class="line"><svg width="12" height="12" viewBox="0 0 12 12"><rect x="1" y="3" width="10" height="8" fill="#fff"/><rect x="3" y="0" width="6" height="4" fill="#fff"/></svg><span>Fax: (954) 555-0129</span></div>
  </div>
  <div class="loc" style="left:811px">
    <h4>Opening Time</h4>
    <div class="line"><span>Monday - Friday &nbsp;: &nbsp;9am to 4:30pm.<br>Saturday - Sunday &nbsp;: &nbsp;Closed</span></div>
  </div>
</footer>

<div class="sec bottom">
  <span>© Copyright 2018 Tor Brook Healthcare. All Rights Reserved.</span>
  <div class="social"><span></span><span></span><span></span><span></span></div>
</div>

</body>
</html>
```